Solar energy proposal for homeowners

I am providing households with solar energy proposals, and I need a high-quality brochure that is packaged cleverly to attract the homeowner's attention. Take a look at the one page solar brochure that I have included to get an idea of text and content.

Target Market(s)

Residential Homeowners

Industry/Entity Type

Solar

Requirements
Must have
• High quality document

```html
<!DOCTYPE html>
<html lang="en">
<head>
<meta charset="utf-8">
<title>Brightvale Energy – Solar for $0 Down</title>
<link rel="stylesheet" href="https://fonts.googleapis.com/css2?family=Cabin:wght@500;600&family=Lato:wght@400;700&family=Tinos:wght@400;700&display=swap">
<style>
  :root {
    --green: #5fd167;
    --green-light: #86d94a;
    --green-text: #4cc85a;
    --teal: #00b4cc;
    --teal-deep: #00a7d2;
    --ink: #111111;
    --body: #4a4a4a;
    --white: #ffffff;
  }
  html, body { margin: 0; padding: 0; overflow: hidden; background: var(--white); }
  .flyer {
    position: relative;
    width: 905px;
    height: 1200px;
    overflow: hidden;
    background: var(--white);
    font-family: "Lato", sans-serif;
  }
  .shapes { position: absolute; inset: 0; }
  .abs { position: absolute; margin: 0; }

  /* Brand */
  .brand { left: 592px; top: 30px; display: flex; align-items: center; gap: 10px; }
  .brand-dot { width: 22px; height: 22px; border-radius: 50%; background: var(--teal); }
  .brand-name { font-family: "Cabin", sans-serif; font-weight: 500; font-size: 30px; color: var(--teal); letter-spacing: 0.5px; }

  /* Hero */
  .hero-title { font-family: "Tinos", serif; font-weight: 700; color: var(--white); line-height: 1; }
  .hero-line1 { left: 42px; top: 46px; font-size: 58px; letter-spacing: 1px; }
  .hero-line2 { left: 42px; top: 133px; font-size: 62px; word-spacing: 14px; }
  .perk { left: 48px; display: flex; align-items: center; gap: 20px; font-family: "Tinos", serif; font-weight: 700; font-size: 39px; color: var(--white); line-height: 1; }
  .perk-icon { width: 26px; height: 26px; }
  .perk-liens { top: 236px; }
  .perk-kidding { top: 293px; }
  .tagline { left: 48px; top: 368px; font-family: "Cabin", sans-serif; font-weight: 600; font-size: 24px; line-height: 38px; color: var(--white); }

  /* Section headings */
  .section-title { font-family: "Cabin", sans-serif; font-weight: 500; font-size: 46px; line-height: 1; color: var(--ink); }
  .section-title .accent { color: var(--teal); font-weight: 600; }
  .services-title { left: 46px; top: 522px; }
  .about-title { left: 452px; top: 632px; font-family: "Tinos", serif; font-weight: 400; font-size: 46px; }
  .about-title .accent { font-weight: 700; }

  /* Services */
  .service { left: 0; width: 420px; }
  .service-title { left: 120px; top: 10px; font-family: "Cabin", sans-serif; font-weight: 500; font-size: 22px; color: var(--teal); white-space: nowrap; }
  .service-text { left: 46px; top: 58px; width: 366px; font-size: 13px; line-height: 22px; color: var(--body); text-align: justify; }
  .service-text.ragged { text-align: left; }
  .service-1 { top: 622px; }
  .service-2 { top: 745px; }
  .service-3 { top: 876px; }
  .service-4 { top: 1000px; }

  /* About */
  .about-text { left: 452px; top: 713px; width: 428px; font-size: 13.6px; line-height: 27.7px; color: var(--body); }
  .about-text .hl { color: var(--green-text); font-weight: 700; }
  .about-text .hl-soft { color: var(--green-text); }

  /* Why choose */
  .why-title { left: 450px; top: 870px; font-family: "Tinos", serif; font-weight: 700; font-size: 47px; color: var(--white); line-height: 1; }
  .why-title .light { font-weight: 400; }
  .benefit { display: flex; align-items: center; gap: 14px; font-size: 15px; color: var(--white); white-space: nowrap; }
  .benefit svg { width: 30px; height: 30px; flex: none; }

  /* Footer */
  .contact { top: 1139px; display: flex; align-items: center; gap: 13px; font-size: 16px; color: var(--white); white-space: nowrap; }
  .contact svg { width: 42px; height: 42px; flex: none; }
</style>
</head>
<body>
<main class="flyer">

  <svg class="shapes" width="905" height="1200" viewBox="0 0 905 1200" aria-hidden="true">
    <defs>
      <linearGradient id="heroGreen" x1="0" y1="0" x2="0" y2="1">
        <stop offset="0" stop-color="#86d94a"/>
        <stop offset="1" stop-color="#4fd37a"/>
      </linearGradient>
      <linearGradient id="whyTeal" x1="0" y1="0" x2="0" y2="1">
        <stop offset="0" stop-color="#00a8d3"/>
        <stop offset="1" stop-color="#00bcc9"/>
      </linearGradient>
      <linearGradient id="footerGreen" x1="0" y1="0" x2="0" y2="1">
        <stop offset="0" stop-color="#7ed84e"/>
        <stop offset="1" stop-color="#55d270"/>
      </linearGradient>
      <linearGradient id="homeScene" x1="0" y1="0" x2="0" y2="1">
        <stop offset="0" stop-color="#9fb4cc"/>
        <stop offset="0.45" stop-color="#5a6f86"/>
        <stop offset="0.8" stop-color="#7a6a5a"/>
        <stop offset="1" stop-color="#6fa7b3"/>
      </linearGradient>
    </defs>

    <!-- hero background -->
    <polygon points="0,0 555,0 505,85 480,85 365,490 50,490 0,565" fill="url(#heroGreen)"/>
    <!-- price band -->
    <polygon points="0,124 358,128 405,202 0,200" fill="var(--teal)"/>
    <!-- services heading underline -->
    <polygon points="52,575 143,575 130,581 52,581" fill="var(--teal)"/>
    <!-- about heading underline -->
    <polygon points="452,689 543,689 530,696 452,696" fill="var(--teal)"/>

    <!-- service tabs -->
    <g fill="var(--teal)">
      <polygon points="0,622 92,622 82,664 0,662"/>
      <polygon points="0,745 92,745 82,787 0,785"/>
      <polygon points="0,876 92,876 82,918 0,916"/>
      <polygon points="0,1000 92,1000 82,1042 0,1040"/>
    </g>
    <!-- service icon badges -->
    <g stroke="var(--white)" stroke-width="3" fill="var(--green)">
      <circle cx="80" cy="649" r="22"/>
      <circle cx="80" cy="773" r="22"/>
      <circle cx="80" cy="904" r="22"/>
      <circle cx="80" cy="1028" r="22"/>
    </g>
    <g fill="none" stroke="var(--white)" stroke-width="1.6" stroke-linecap="round" stroke-linejoin="round">
      <!-- pricing: hand with coin -->
      <circle cx="82" cy="643" r="6"/>
      <path d="M80 641 h3 a1.5 1.5 0 0 1 0 3 h-2 a1.5 1.5 0 0 0 0 3 h3"/>
      <path d="M69 653 l5 -2 h8 l5 -3 M69 659 h10 l10 -6"/>
      <!-- installation: gear -->
      <circle cx="80" cy="773" r="5"/>
      <circle cx="80" cy="773" r="10" stroke-dasharray="4 3"/>
      <!-- local: star medal -->
      <circle cx="80" cy="900" r="9"/>
      <path d="M80 895 l1.6 3.3 3.6 .5 -2.6 2.5 .6 3.6 -3.2 -1.7 -3.2 1.7 .6 -3.6 -2.6 -2.5 3.6 -.5z"/>
      <path d="M75 908 l-2 8 4 -2 3 3 M85 908 l2 8 -4 -2 -3 3"/>
      <!-- eco: leaves -->
      <path d="M72 1034 c0 -6 5 -8 8 -8 c0 6 -4 9 -8 8z M88 1034 c0 -6 -5 -8 -8 -8 c0 6 4 9 8 8z M80 1026 v-6"/>
      <path d="M75 1020 a6 6 0 0 1 10 0"/>
    </g>

    <!-- why choose panel -->
    <polygon points="449,848 853,848 880,874 905,874 905,1123 360,1123" fill="url(#whyTeal)"/>
    <polygon points="457,932 547,932 533,939 457,939" fill="var(--green-light)"/>

    <!-- footer -->
    <rect x="0" y="1123" width="905" height="77" fill="url(#footerGreen)"/>
    <g stroke="var(--white)" stroke-width="2" stroke-dasharray="5 5">
      <line x1="322" y1="1140" x2="322" y2="1186"/>
      <line x1="551" y1="1140" x2="551" y2="1186"/>
    </g>
  </svg>

  <!-- home photo area -->
  <svg class="abs" style="left:0;top:0" width="905" height="600" viewBox="0 0 905 600" role="img" aria-label="Photo of a modern gabled house at dusk with solar panels on the dark roof, a wall-mounted inverter and a pool in front">
    <polygon points="490,97 905,97 905,555 680,555 635,595 345,595" fill="url(#homeScene)"/>
  </svg>

  <!-- brand -->
  <div class="abs brand">
    <span class="brand-dot"></span>
    <span class="brand-name">Brightvale Energy</span>
  </div>

  <!-- hero -->
  <h1 class="abs hero-title hero-line1">SOLAR FOR</h1>
  <p class="abs hero-title hero-line2">$0 DOWN</p>

  <p class="abs perk perk-liens">
    <svg class="perk-icon" viewBox="0 0 26 26" aria-hidden="true"><circle cx="13" cy="13" r="13" fill="#fff"/><path d="M7 13 h11 M14 9 l4 4 -4 4" stroke="#4fc66a" stroke-width="2.4" fill="none" stroke-linecap="round" stroke-linejoin="round"/></svg>
    NO LIENS
  </p>
  <p class="abs perk perk-kidding">
    <svg class="perk-icon" viewBox="0 0 26 26" aria-hidden="true"><circle cx="13" cy="13" r="13" fill="#fff"/><path d="M7 13 h11 M14 9 l4 4 -4 4" stroke="#4fc66a" stroke-width="2.4" fill="none" stroke-linecap="round" stroke-linejoin="round"/></svg>
    NO KIDDING
  </p>

  <p class="abs tagline">Power Your Future with<br>Brightvale Energy</p>

  <!-- services -->
  <h2 class="abs section-title services-title">Our <span class="accent">Services</span></h2>

  <section class="abs service service-1">
    <h3 class="abs service-title">Affordable &amp; Transparent</h3>
    <p class="abs service-text">Simple pricing, no hidden fees and a fixed monthly rate lower than typical energy bills.</p>
  </section>
  <section class="abs service service-2">
    <h3 class="abs service-title">Expert Installation</h3>
    <p class="abs service-text">Certified professionals handle installation, maintenance, and repairs end to end.</p>
  </section>
  <section class="abs service service-3">
    <h3 class="abs service-title">Local Expertise</h3>
    <p class="abs service-text ragged">Florida-based team that understands the needs of Orlando<br>&nbsp;and statewide homeowners.</p>
  </section>
  <section class="abs service service-4">
    <h3 class="abs service-title">Eco-Friendly</h3>
    <p class="abs service-text ragged">Clean, renewable solar energy that helps reduce your<br>&nbsp;carbon footprint.</p>
  </section>

  <!-- about -->
  <h2 class="abs section-title about-title">About <span class="accent">Us</span></h2>
  <p class="abs about-text">At <span class="hl">Brightvale Energy</span>, our mission is to make solar simple and accessible for everyone. No high-pressure sales-just the information you need to make a smart choice. With our solar <span class="hl">rental program,</span> you can lower your monthly energy costs and <span class="hl-soft">pay less</span> than your current electricity bill</p>

  <!-- why choose -->
  <h2 class="abs why-title"><span class="light">Why</span> Choose Us?</h2>

  <p class="abs benefit" style="left:452px;top:973px">
    <svg viewBox="0 0 30 30" aria-hidden="true"><circle cx="15" cy="15" r="15" fill="#fff"/><g fill="none" stroke="#00b4cc" stroke-width="1.6" stroke-linecap="round"><circle cx="15" cy="15" r="8"/><path d="M9 21 L21 9 M17 11.5 h-3 a1.5 1.5 0 0 0 0 3 h2 a1.5 1.5 0 0 1 0 3 h-3"/></g></svg>
    No financing
  </p>
  <p class="abs benefit" style="left:452px;top:1010px">
    <svg viewBox="0 0 30 30" aria-hidden="true"><circle cx="15" cy="15" r="15" fill="#fff"/><path d="M8 15 l7 -6 7 6 M10 13.5 v7 h10 v-7 M13.5 20.5 v-4 h3 v4" fill="none" stroke="#00b4cc" stroke-width="1.6" stroke-linejoin="round" stroke-linecap="round"/></svg>
    No liens
  </p>
  <p class="abs benefit" style="left:452px;top:1047px">
    <svg viewBox="0 0 30 30" aria-hidden="true"><circle cx="15" cy="15" r="15" fill="#fff"/><path d="M11 8 h8 v7 h3 l-7 7 -7 -7 h3z" fill="none" stroke="#00b4cc" stroke-width="1.6" stroke-linejoin="round"/></svg>
    No down payment
  </p>
  <p class="abs benefit" style="left:656px;top:973px">
    <svg viewBox="0 0 30 30" aria-hidden="true"><circle cx="15" cy="15" r="15" fill="#fff"/><path d="M9 14 l6 -5 6 5 M11 12.5 v5 h8 v-5 M7 20 h5 l3 2 h8" fill="none" stroke="#00b4cc" stroke-width="1.6" stroke-linejoin="round" stroke-linecap="round"/></svg>
    No insurance costs
  </p>
  <p class="abs benefit" style="left:656px;top:1010px">
    <svg viewBox="0 0 30 30" aria-hidden="true"><circle cx="15" cy="15" r="15" fill="#fff"/><g fill="none" stroke="#00b4cc" stroke-width="1.6" stroke-linecap="round"><path d="M21.5 12 a7.5 7.5 0 1 0 0.5 5"/><path d="M22 8.5 v4 h-4"/><path d="M17 13 a3 3 0 1 0 0 4"/></g></svg>
    No long-term commitment
  </p>
  <p class="abs benefit" style="left:656px;top:1047px">
    <svg viewBox="0 0 30 30" aria-hidden="true"><circle cx="15" cy="15" r="15" fill="#fff"/><g fill="none" stroke="#00b4cc" stroke-width="1.6" stroke-linecap="round"><circle cx="15" cy="15" r="8"/><path d="M17 11.5 h-3 a1.5 1.5 0 0 0 0 3 h2 a1.5 1.5 0 0 1 0 3 h-3 M15 10 v1.5 M15 17.5 v1.5"/></g></svg>
    No maintenance costs
  </p>

  <!-- contact -->
  <p class="abs contact" style="left:47px">
    <svg viewBox="0 0 42 42" aria-hidden="true"><circle cx="21" cy="21" r="21" fill="#fff"/><path d="M21 11 a7 7 0 0 1 7 7 c0 5 -7 13 -7 13 s-7 -8 -7 -13 a7 7 0 0 1 7 -7z" fill="#00b4cc"/><circle cx="21" cy="18" r="2.6" fill="#fff"/></svg>
    123 Anywhere St., Any City
  </p>
  <p class="abs contact" style="left:352px">
    <svg viewBox="0 0 42 42" aria-hidden="true"><circle cx="21" cy="21" r="21" fill="#fff"/><path d="M15 12 l4 -1 2.5 5.5 -2.5 2 c1 2.5 2.8 4.3 5.5 5.5 l2 -2.5 5.5 2.5 -1 4 c-9 1 -17 -7 -16 -16z" fill="#00b4cc"/></svg>
    (407)555-0142
  </p>
  <p class="abs contact" style="left:581px">
    <svg viewBox="0 0 42 42" aria-hidden="true"><circle cx="21" cy="21" r="21" fill="#fff"/><g fill="none" stroke="#00b4cc" stroke-width="1.8" stroke-linejoin="round"><rect x="11" y="14" width="20" height="14"/><path d="M11 14 l10 8 10 -8 M11 28 l7 -7 M31 28 l-7 -7"/></g></svg>
    www.brightvaleenergy.com
  </p>

</main>
</body>
</html>
```